Online Prescription Eyeglass Lens Company Needs a Website

*Update new name to ClearPair. Thx

We are eye doctors with a lab that need a website for a new company based in Southern California called ClearPair. We replace old prescription lenses with new ones next day for most lenses. Patients select the lenses and give us the prescription. We then send a box with a prepaid shipping label. Place the frames in the box and drop them in the mail to our lab. We will custom make new lenses, fit them back into your frames and send them back to you. We would like to compete with www.vizora.com and offer affordable lenses for single vision, bifocal, progressive, sunglass lenses at an affordable price with next day shipping.
Updates

Hi Designers, We have a new name called ClearPair. Can we have the website design reflect the new name and we'll pick our favorites. Thx

Update: The new name is OptiNova . I have not made very many changes or feedback to the submissions because we were bidding for a .com. We won and our new name is OptiNova . This is the last name change.. Please have the website reflect the new name and I'll be providing feedback on the websites . ( I have a separate project for the logo people are working on, so don't worry about creating a logo). Look forward to the submissions. Thanks everyone.

Hi, Just leave the name as ClearPair for now. I will narrow down top designs tonight. Thx

Target Market(s)

Anyone that wears prescription or nonprescription glasses or sunglasses that want next day shipping.

Industry/Entity Type

Eyewear

Number of Pages Required

4 page

Font styles to use
Serif

Colors

Designer to choose colors to be used in the design.

Requirements
Must have
• I need a website that can compete with https://www.vizora.com/.
• We are different from vizora because we can offer same day service or next day shipping.
• It needs to have website that offers the lenses available listed below.
• Needs to be able to upload a prescription and payment feature.
• Pictures of different types of options with small info about each lens option.
• Template Pricing (just use numbers from $79-$179 for now)
• SINGLE VISION LENSES
• HIGH INDEX LENSES
• READING LENSES
• DIGITAL HD PROGRESSIVE LENSES
• RX & NON-RX SUNGLASSES
• RX & NON-RX POLARIZED SUNGLASSES
• COMPUTER LENSES
• TRANSITION LENSES
• BI-FOCAL LENSES

```html
<!DOCTYPE html>
<html lang="en">
<head>
<meta charset="utf-8">
<title>ClearPair — Prescription Lenses</title>
<link rel="stylesheet" href="https://fonts.googleapis.com/css2?family=Oswald:wght@500&family=Playfair+Display:wght@700&family=Lora:wght@400;500;600&family=Roboto:wght@400;500;700&display=swap">
<style>
  :root {
    --teal: #2cc8d6;
    --teal-deep: #1fb4c2;
    --ink: #1e1e1e;
    --muted: #555;
    --rule: #cfd6d8;
    --card-line: #d6d6d6;
    --price-grey: #a9a9a9;
    --footer: #2b2b2b;
    --footer-base: #0f4f56;
    --white: #ffffff;
  }
  * { box-sizing: border-box; margin: 0; padding: 0; }
  html, body { width: 1200px; height: 2936px; overflow: hidden; background: var(--white); }
  body { position: relative; font-family: "Lora", Georgia, serif; color: var(--ink); }
  .abs { position: absolute; }

  /* header */
  .site-header { left: 0; top: 0; width: 1200px; height: 72px; background: #f7f7f7; }
  .brand { left: 88px; top: 16px; font-family: "Roboto", Arial, sans-serif; font-weight: 700; font-size: 30px; color: var(--teal); letter-spacing: .3px; }
  .header-phone { left: 758px; top: 25px; font-family: "Roboto", Arial, sans-serif; font-size: 19px; color: #222; display: flex; align-items: center; gap: 6px; }
  .btn-order { left: 926px; top: 20px; width: 114px; height: 34px; border-radius: 17px; background: var(--teal); color: #fff; font-size: 15px; font-family: "Lora", serif; display: flex; align-items: center; justify-content: center; }
  .menu-icon { left: 1080px; top: 26px; }

  /* hero */
  .hero { left: 0; top: 72px; width: 1200px; height: 593px; background: linear-gradient(100deg, #cfd4d7 0%, #9aa3a9 35%, #6d7a86 65%, #38506b 100%); }
  .hero-shade { left: 0; top: 72px; width: 1200px; height: 593px; background: rgba(20,25,30,.25); }
  .hero-title { left: 0; top: 280px; width: 1200px; text-align: center; font-family: "Oswald", sans-serif; font-weight: 500; font-size: 64px; color: #fff; letter-spacing: 1px; }
  .hero-sub { left: 0; top: 366px; width: 1200px; text-align: center; font-size: 25px; color: #fff; }
  .btn-collection { left: 499px; top: 430px; width: 200px; height: 50px; border-radius: 25px; background: var(--teal); color: #fff; font-size: 17px; font-weight: 500; display: flex; align-items: center; justify-content: center; }

  /* process */
  .section-title { font-family: "Playfair Display", serif; font-weight: 700; font-size: 29px; letter-spacing: .5px; color: #222; }
  .process-title { left: 0; top: 726px; width: 1200px; text-align: center; }
  .title-rule { left: 497px; top: 768px; }
  .step-ring { width: 170px; height: 170px; border-radius: 50%; border: 7px solid var(--teal); top: 813px; display: flex; align-items: center; justify-content: center; }
  .step-ring .inner { width: 138px; height: 138px; border-radius: 50%; border: 5px solid var(--teal); display: flex; align-items: center; justify-content: center; background: #fff; }
  .step-link { top: 897px; height: 0; border-top: 2px dashed #777; }
  .step-text { top: 1006px; width: 320px; text-align: center; font-size: 18px; line-height: 26px; font-weight: 500; color: #111; }

  /* prescription band */
  .band-photo { left: 600px; top: 1149px; width: 600px; height: 378px; background: linear-gradient(120deg, #c9b5a6 0%, #8d7a6f 45%, #d9d6d4 75%, #5e3b35 100%); }
  .band-panel { left: 0; top: 1149px; width: 1200px; height: 378px; }
  .band-text { left: 84px; top: 1214px; width: 520px; font-size: 25px; line-height: 38px; color: #fff; font-weight: 500; }
  .btn-upload { left: 86px; top: 1401px; width: 214px; height: 46px; border-radius: 23px; border: 2px solid #1d3a3e; color: #10262a; font-size: 16px; font-weight: 600; display: flex; align-items: center; justify-content: center; }

  /* lens cards */
  .lens-card { top: 1599px; width: 237px; height: 256px; border: 1.5px solid var(--card-line); background: #fff; }
  .lens-swatch { position: absolute; left: 58px; top: 9px; width: 120px; height: 106px; border-radius: 50%; }
  .lens-name { position: absolute; left: 0; top: 133px; width: 100%; text-align: center; font-size: 17px; font-weight: 500; color: #222; }
  .lens-rule { position: absolute; left: 98px; top: 166px; width: 40px; height: 2px; background: var(--teal); }
  .lens-copy { position: absolute; left: 20px; top: 178px; width: 197px; text-align: center; font-size: 12.5px; line-height: 22px; color: #333; }
  .price-bar { left: 86px; top: 1859px; width: 237px; height: 35px; display: flex; }
  .price-bar .price { width: 115px; background: var(--price-grey); color: #fff; font-family: "Roboto", sans-serif; font-size: 18px; font-weight: 500; display: flex; align-items: center; justify-content: center; }
  .price-bar .order { flex: 1; background: var(--teal); color: #fff; font-size: 15px; display: flex; align-items: center; justify-content: center; }
  .slider-arrow { top: 1702px; }

  /* feature rows */
  .feature-photo { width: 600px; }
  .feature-title { font-size: 25px; }
  .feature-rule { width: 64px; height: 2px; background: var(--teal); }
  .feature-copy { width: 490px; font-family: "Roboto", Arial, sans-serif; font-size: 12.7px; line-height: 22px; color: #333; text-align: justify; }
  .btn-shop { width: 116px; height: 36px; border-radius: 18px; background: var(--teal); color: #fff; font-family: "Roboto", sans-serif; font-weight: 700; font-size: 13px; display: flex; align-items: center; justify-content: center; }

  /* footer */
  .site-footer { left: 0; top: 2777px; width: 1200px; height: 113px; background: var(--footer); }
  .footer-base { left: 0; top: 2890px; width: 1200px; height: 46px; background: var(--footer-base); }
  .footer-contact { left: 88px; font-family: "Roboto", sans-serif; font-size: 15px; color: #fff; display: flex; align-items: center; gap: 14px; }
  .footer-nav { top: 2824px; font-family: "Roboto", sans-serif; font-size: 12.5px; color: #ddd; display: flex; gap: 30px; }
  .footer-brand { left: 503px; top: 2834px; width: 200px; text-align: center; font-family: "Roboto", sans-serif; font-size: 22px; letter-spacing: 4px; color: var(--teal); }
  .social { top: 2828px; display: flex; gap: 20px; }
  .social span { width: 20px; height: 20px; border-radius: 50%; background: #e6e6e6; display: block; }
  .copyright { left: 880px; top: 2904px; font-family: "Roboto", sans-serif; font-size: 12px; color: #9fb9bc; }
</style>
</head>
<body>

<header class="site-header abs">
  <div class="brand abs">ClearPair</div>
  <div class="header-phone abs">
    <svg width="16" height="16" viewBox="0 0 24 24"><path fill="#222" d="M6.6 10.8a15.1 15.1 0 0 0 6.6 6.6l2.2-2.2c.3-.3.7-.4 1-.2 1.1.4 2.3.6 3.6.6.6 0 1 .4 1 1V20c0 .6-.4 1-1 1A17 17 0 0 1 3 4c0-.6.4-1 1-1h3.5c.6 0 1 .4 1 1 0 1.3.2 2.5.6 3.6.1.3 0 .7-.2 1z"/></svg>
    555-0142-000
  </div>
  <div class="btn-order abs">Order Now</div>
  <svg class="menu-icon abs" width="34" height="22" viewBox="0 0 34 22"><rect width="34" height="4" rx="1" fill="#333"/><rect y="9" width="34" height="4" rx="1" fill="#333"/><rect y="18" width="34" height="4" rx="1" fill="#333"/></svg>
</header>

<section>
  <div class="hero abs" role="img" aria-label="Photo of an eye doctor and a technician working at an optical lab instrument"></div>
  <div class="hero-shade abs"></div>
  <h1 class="hero-title abs">WE ARE DIFFEREN</h1>
  <p class="hero-sub abs">We offer same day service or next day shipping.</p>
  <div class="btn-collection abs">SEE COLLECTION</div>
</section>

<section>
  <h2 class="section-title process-title abs">OUR PROCESS</h2>
  <svg class="title-rule abs" width="206" height="14" viewBox="0 0 206 14">
    <line x1="0" y1="7" x2="88" y2="7" stroke="#cfd6d8" stroke-width="2"/>
    <ellipse cx="103" cy="7" rx="13" ry="5.5" fill="none" stroke="#cfd6d8" stroke-width="2"/>
    <line x1="118" y1="7" x2="206" y2="7" stroke="#cfd6d8" stroke-width="2"/>
  </svg>

  <div class="step-link abs" style="left:342px;width:170px"></div>
  <div class="step-link abs" style="left:694px;width:170px"></div>

  <div class="step-ring abs" style="left:164px"><div class="inner">
    <svg width="52" height="64" viewBox="0 0 52 64"><rect x="3" y="3" width="46" height="58" fill="none" stroke="#222" stroke-width="3"/><path d="M13 15h8M17 11v8" stroke="#222" stroke-width="3"/><path d="M12 30h28M12 38h28M12 46h28M12 54h18" stroke="#222" stroke-width="2.5"/></svg>
  </div></div>
  <div class="step-ring abs" style="left:516px"><div class="inner">
    <svg width="74" height="48" viewBox="0 0 74 48"><path d="M6 30c6 12 56 12 62 0" fill="none" stroke="#222" stroke-width="3"/><ellipse cx="37" cy="30" rx="31" ry="8" fill="none" stroke="#222" stroke-width="3"/><path d="M24 26c2-14 22-24 34-20 6 3-4 14-20 20" fill="none" stroke="#222" stroke-width="3"/></svg>
  </div></div>
  <div class="step-ring abs" style="left:868px"><div class="inner">
    <svg width="62" height="62" viewBox="0 0 62 62"><path d="M31 4 58 16 31 28 4 16z" fill="#555"/><path d="M4 16v30l27 13V28z" fill="#1b1b1b"/><path d="M58 16v30L31 59V28z" fill="#333"/></svg>
  </div></div>

  <p class="step-text abs" style="left:89px">We replace old prescription lenses with new ones next day<br>for most lenses</p>
  <p class="step-text abs" style="left:441px">Patients select the lenses and give us the prescription.</p>
  <p class="step-text abs" style="left:793px">We then send a box with a prepaid shipping label.</p>
</section>

<section>
  <div class="band-photo abs" role="img" aria-label="Photo of an optician's hands holding a trial lens frame"></div>
  <svg class="band-panel abs" width="1200" height="378" viewBox="0 0 1200 378"><polygon points="0,0 665,0 622,378 0,378" fill="#2cc8d6"/></svg>
  <p class="band-text abs">We replace old prescription lenses with new ones next day for most lenses. Patients select the lenses and give us the prescription.</p>
  <div class="btn-upload abs">Upload a Prescription</div>
</section>

<section>
  <svg class="slider-arrow abs" style="left:40px" width="20" height="48" viewBox="0 0 20 48"><path d="M18 2 3 24l15 22" fill="none" stroke="#555" stroke-width="2"/></svg>
  <svg class="slider-arrow abs" style="left:1138px" width="20" height="48" viewBox="0 0 20 48"><path d="M2 2l15 22L2 46" fill="none" stroke="#2cc8d6" stroke-width="2"/></svg>

  <article class="lens-card abs" style="left:86px">
    <div class="lens-swatch" role="img" aria-label="Single vision lens" style="background:radial-gradient(circle at 40% 35%, #ffffff, #e3e7e8 60%, #b8bfc1)"></div>
    <h3 class="lens-name">SINGLE VISION LENSES</h3><div class="lens-rule"></div>
    <p class="lens-copy">Lorem Ipsum is simply dummy text of the printing and typesetting industry</p>
  </article>
  <article class="lens-card abs" style="left:350px">
    <div class="lens-swatch" role="img" aria-label="High index lens" style="top:20px;left:30px;width:176px;height:86px;background:radial-gradient(ellipse at 50% 40%, #ffffff, #e4e8e0 55%, #a9ad98)"></div>
    <h3 class="lens-name">HIGH INDEX LENSES</h3><div class="lens-rule"></div>
    <p class="lens-copy">Lorem Ipsum is simply dummy text of the printing and typesetting industry</p>
  </article>
  <article class="lens-card abs" style="left:613px">
    <div class="lens-swatch" role="img" aria-label="Reading lens" style="left:64px;width:110px;background:radial-gradient(circle at 45% 40%, #eaf6fc, #c9e6f3 60%, #8fb8cc)"></div>
    <h3 class="lens-name">READING LENSES</h3><div class="lens-rule"></div>
    <p class="lens-copy">Lorem Ipsum is simply dummy text of the printing and typesetting industry</p>
  </article>
  <article class="lens-card abs" style="left:875px">
    <div class="lens-swatch" role="img" aria-label="Computer lens" style="background:radial-gradient(circle at 40% 35%, #ffffff, #eceeee 60%, #bcc2c3)"></div>
    <h3 class="lens-name">COMPUTER LENSES</h3><div class="lens-rule"></div>
    <p class="lens-copy">Lorem Ipsum is simply dummy text of the printing and typesetting industry</p>
  </article>

  <div class="price-bar abs"><div class="price">$79</div><div class="order">Order Now</div></div>
</section>

<section>
  <div class="feature-photo abs" style="left:0;top:1977px;height:375px;background:linear-gradient(110deg,#e8ece9 0%,#a8b8b2 40%,#4f7f80 70%,#c9d3d1 100%)" role="img" aria-label="Photo of a smiling man wearing designer glasses"></div>
  <h2 class="section-title feature-title abs" style="left:628px;top:2028px">DESIGNER GLASSES</h2>
  <div class="feature-rule abs" style="left:628px;top:2070px"></div>
  <p class="feature-copy abs" style="left:628px;top:2096px">Lorem Ipsum is simply dummy text of the printing and typesetting industry. Lorem Ipsum has been the industry's standard dummy text ever since the 1500s, when an unknown printer took a galley of type and scrambled it to make a type specimen book. It has survived not only five centuries, but also the leap into electronic typesetting, remaining essentially unchanged. It was popularised in the</p>
  <div class="btn-shop abs" style="left:628px;top:2234px">SHOP NOW</div>

  <div class="feature-photo abs" style="left:600px;top:2352px;height:372px;background:linear-gradient(120deg,#dfe2e6 0%,#c2b3b3 40%,#7a5e58 65%,#d8c9c0 100%)" role="img" aria-label="Photo of a woman in a beanie wearing sunglasses"></div>
  <h2 class="section-title feature-title abs" style="left:86px;top:2423px">DESIGNER SUNGLASSES</h2>
  <div class="feature-rule abs" style="left:86px;top:2465px"></div>
  <p class="feature-copy abs" style="left:86px;top:2491px">Lorem Ipsum is simply dummy text of the printing and typesetting industry. Lorem Ipsum has been the industry's standard dummy text ever since the 1500s, when an unknown printer took a galley of type and scrambled it to make a type specimen book. It has survived not only five centuries, but also the leap into electronic typesetting, remaining essentially unchanged. It was popularised in the</p>
  <div class="btn-shop abs" style="left:86px;top:2629px">SHOP NOW</div>
</section>

<footer>
  <div class="site-footer abs"></div>
  <div class="footer-contact abs" style="top:2804px">
    <svg width="26" height="22" viewBox="0 0 26 22"><rect x="2" y="5" width="22" height="15" fill="none" stroke="#fff" stroke-width="2"/><path d="M2 5l11 8 11-8" fill="none" stroke="#fff" stroke-width="2"/></svg>
    info@clearpair-mail.com
  </div>
  <div class="footer-contact abs" style="top:2843px">
    <svg width="26" height="24" viewBox="0 0 24 24"><path fill="#fff" d="M6.6 10.8a15.1 15.1 0 0 0 6.6 6.6l2.2-2.2c.3-.3.7-.4 1-.2 1.1.4 2.3.6 3.6.6.6 0 1 .4 1 1V20c0 .6-.4 1-1 1A17 17 0 0 1 3 4c0-.6.4-1 1-1h3.5c.6 0 1 .4 1 1 0 1.3.2 2.5.6 3.6.1.3 0 .7-.2 1z"/></svg>
    555.010.2938
  </div>
  <nav class="footer-nav abs" style="left:335px"><span>Home</span><span>Product</span><span>Features</span></nav>
  <div class="footer-brand abs">CLEARPAIR</div>
  <nav class="footer-nav abs" style="left:699px"><span>About us</span><span>Partners</span><span>Company</span></nav>
  <div class="social abs" style="left:1012px"><span></span><span></span><span></span></div>
  <div class="footer-base abs"></div>
  <p class="copyright abs">© 2017 company name. All rights reserved</p>
</footer>

</body>
</html>
```